A5 Flyer for Window Cleaning Company

2 sided Flyer design required for window cleaning company. One side to include we use traditional and hot water fed pole window cleaning systems, conservatory cleaning, and fascia and soffit cleaning. The other side to be for Gutter cleaning. See the must haves section of project brief for more info. Mixture of some images and text for both sides. ( do not have to use all images supplied). The flyer will be used to promote the business to new residential customers.

Target Market(s)

Private households/new customers

Industry/Entity Type

Window Cleaning

Font styles to use
Serif

Requirements
Must have
• Company address ( 7 Old Pennick Court Harlow Street Edinburgh EH4 9RQ
Phone numbers( 0131 482 7719 0800 061 2287).
Website and email address ( info@falconbright-cleaning.example)
Excellent Customer Service. Competitive prices. Established 1994.
Side 1of flyer = Falconbright Window Cleaning Side 2 of flyer Falconbright Gutter Cleaning.
Nice to have
• Professional look.

```html
<!DOCTYPE html>
<html lang="en">
<head>
<meta charset="utf-8">
<title>Falconbright Window Cleaning – Gutter Cleaning Flyer</title>
<link rel="stylesheet" href="https://fonts.googleapis.com/css2?family=Jost:wght@400;500;600&display=swap">
<style>
  :root {
    --navy: #1a1f7a;
    --blue: #2e3a9e;
    --sky: #8cc4ee;
    --rule: #9fd3f0;
    --paper: #ffffff;
    --photo-sky: #5f97d2;
    --photo-sky-light: #b9d3ec;
    --photo-wall: #4e3f3a;
    --photo-wall-light: #6e5d55;
    --photo-gutter: #e4e6e3;
    --photo-leaf: #b8652a;
    --photo-glove: #9a9c98;
  }
  * { margin: 0; padding: 0; box-sizing: border-box; }
  html, body { width: 848px; height: 1200px; overflow: hidden; background: var(--paper); }
  .flyer {
    position: relative; width: 848px; height: 1200px; background: var(--paper);
    font-family: "Jost", "Futura", sans-serif; color: var(--navy);
  }
  .photo-column { position: absolute; left: 0; top: 0; width: 366px; height: 1200px; }
  .photo-column svg { display: block; }
  .info-panel {
    position: absolute; left: 444px; top: 170px; width: 312px; height: 866px;
    border: 2px solid var(--blue); padding: 18px 14px 0;
  }
  .brand { display: flex; flex-direction: column; align-items: center; }
  .brand-square { width: 282px; height: 166px; background: var(--sky); }
  .brand-name {
    margin-top: 24px; width: 282px; text-align: center;
    font-weight: 600; font-size: 34px; line-height: 1.12; color: var(--navy);
  }
  .service {
    margin-top: 36px; font-size: 27px; line-height: 1.2; font-weight: 400;
    color: var(--blue); text-transform: uppercase; letter-spacing: 0.3px;
  }
  .address { margin-top: 22px; font-size: 20px; line-height: 1.35; color: var(--navy); }
  .rule { height: 2px; background: var(--rule); margin: 14px 0; }
  .contact-row { display: flex; gap: 14px; align-items: flex-start; font-size: 20px; }
  .contact-label { width: 72px; flex: none; }
  .phones { font-weight: 600; font-size: 24px; line-height: 1.45; letter-spacing: 0.5px; }
  .email { font-size: 15px; line-height: 1.45; white-space: nowrap; padding-top: 3px; }
  .tagline { font-size: 21px; line-height: 1.3; color: var(--navy); white-space: nowrap; }
</style>
</head>
<body>
<div class="flyer">
  <div class="photo-column">
    <svg width="366" height="1200" viewBox="0 0 366 1200">
      <defs>
        <linearGradient id="house-photo" x1="0" y1="0" x2="0.4" y2="1">
          <stop offset="0" stop-color="var(--photo-sky)"/>
          <stop offset="0.28" stop-color="var(--photo-sky-light)"/>
          <stop offset="0.42" stop-color="var(--photo-wall)"/>
          <stop offset="1" stop-color="var(--photo-wall-light)"/>
        </linearGradient>
        <linearGradient id="gutter-photo" x1="0" y1="0" x2="1" y2="1">
          <stop offset="0" stop-color="var(--photo-gutter)"/>
          <stop offset="0.4" stop-color="var(--photo-leaf)"/>
          <stop offset="0.7" stop-color="var(--photo-glove)"/>
          <stop offset="1" stop-color="var(--photo-gutter)"/>
        </linearGradient>
      </defs>
      <rect role="img" aria-label="Photo of a window cleaner on a ladder clearing a house gutter with a long pole under a blue sky" x="0" y="0" width="366" height="720" fill="url(#house-photo)"/>
      <path role="img" aria-label="Photo of a gloved hand lifting autumn leaves out of a white roof gutter" d="M0 720 Q 160 610 366 650 L366 1200 L0 1200 Z" fill="url(#gutter-photo)"/>
    </svg>
  </div>

  <section class="info-panel">
    <div class="brand">
      <div class="brand-square"></div>
      <div class="brand-name">Falconbright Window Cleaning</div>
    </div>

    <h1 class="service">Gutter and Rhone Cleaning</h1>

    <p class="address">Address: 7 Old Pennick Court<br>Harlow Street<br>Edinburgh EH4 9RQ</p>

    <div class="rule"></div>
    <div class="contact-row">
      <span class="contact-label">Phone:</span>
      <div class="phones">0131 482 7719<br>0800 061 2287</div>
    </div>
    <div class="rule"></div>
    <div class="contact-row">
      <span class="contact-label">Email:</span>
      <span class="email">info@falconbright-<br>cleaning.example</span>
    </div>
    <div class="rule"></div>

    <p class="tagline">Excellent Customer Service.<br>Competitive prices.<br>Established 1994</p>
  </section>
</div>
</body>
</html>
```